Business cards for Brightmere Consulting with the following info for the front side:

Brightmere Consulting
Executive Coaching and Human Capital Strategy
www.brightmere.example

Rosalind Feyvette
Principal
rosalind@brightmere.example
+1 604 555 0172

Black background, text using the colours of the logo - enclosed.

The back side of the business card should feature the logo in the middle, with "Executive Coaching and Human Capital Strategy" on top and "www.brightmere.example" below.

```html
<!DOCTYPE html>
<html lang="en">
<head>
<meta charset="utf-8">
<title>Brightmere Consulting — Business Cards</title>
<link rel="stylesheet" href="https://fonts.googleapis.com/css2?family=Roboto:wght@400;500;700&display=swap">
<style>
  :root {
    --backdrop: #e8e8e8;
    --card-white: #ffffff;
    --card-black: #1b1b1b;
    --brand-blue: #2b9fd4;
    --brand-yellow: #f5b40c;
    --mark-grey: #3b3b3b;
    --edge-yellow: #f2b705;
  }
  * { box-sizing: border-box; margin: 0; padding: 0; }
  html, body { width: 1200px; height: 801px; overflow: hidden; }
  body {
    background: var(--backdrop);
    font-family: "Roboto", Arial, sans-serif;
    position: relative;
  }
  .card {
    position: absolute;
    top: 250px;
    width: 520px;
    height: 300px;
    border-bottom: 5px solid var(--edge-yellow);
    box-shadow: 0 6px 18px rgba(0,0,0,0.12);
  }
  /* Contact side */
  .card--contact { left: 60px; background: var(--card-white); }
  .brand {
    position: absolute;
    display: flex;
    align-items: center;
    gap: 10px;
  }
  .brand__dot {
    width: 34px; height: 34px;
    border-radius: 50%;
    border: 3px solid currentColor;
  }
  .brand__name {
    font-weight: 500;
    letter-spacing: 1px;
    text-transform: uppercase;
  }
  .card--contact .brand { top: 38px; right: 38px; color: var(--brand-blue); }
  .card--contact .brand__name { font-size: 30px; }
  .rule-top {
    position: absolute;
    top: 96px; left: 60px; right: 38px;
    height: 1.5px; background: var(--brand-blue);
  }
  .person { position: absolute; left: 38px; top: 160px; }
  .person__name { color: var(--brand-yellow); font-weight: 700; font-size: 22px; }
  .person__title { color: var(--brand-blue); font-size: 14px; margin-top: 2px; }
  .rule-short { width: 220px; height: 1.5px; background: var(--brand-blue); margin: 10px 0 10px; }
  .contacts { list-style: none; }
  .contacts li {
    display: flex; align-items: center; gap: 10px;
    color: var(--brand-blue); font-size: 14px; line-height: 22px;
  }
  .contacts svg { width: 12px; height: 12px; fill: var(--brand-yellow); flex: none; }
  .accent { color: var(--brand-yellow); }

  /* Brand side */
  .card--brand { left: 620px; background: var(--card-black); text-align: center; }
  .card--brand .brand { top: 92px; left: 0; right: 0; justify-content: center; color: var(--mark-grey); }
  .card--brand .brand__dot { width: 44px; height: 44px; }
  .card--brand .brand__name { font-size: 36px; }
  .tagline {
    position: absolute; left: 0; right: 0; top: 190px;
    color: var(--brand-blue); font-size: 16px;
  }
  .web {
    position: absolute; left: 0; right: 0; top: 216px;
    color: var(--brand-blue); font-size: 15px;
  }
</style>
</head>
<body>
  <section class="card card--contact">
    <div class="brand">
      <span class="brand__dot"></span>
      <span class="brand__name">Brightmere</span>
    </div>
    <div class="rule-top"></div>
    <div class="person">
      <p class="person__name">Rosalind Feyvette</p>
      <p class="person__title">Principal</p>
      <div class="rule-short"></div>
      <ul class="contacts">
        <li><svg viewBox="0 0 24 24" aria-hidden="true"><path d="M6.6 10.8a15 15 0 0 0 6.6 6.6l2.2-2.2a1 1 0 0 1 1-.25 11.4 11.4 0 0 0 3.6.57 1 1 0 0 1 1 1V20a1 1 0 0 1-1 1A17 17 0 0 1 3 4a1 1 0 0 1 1-1h3.5a1 1 0 0 1 1 1c0 1.25.2 2.45.57 3.6a1 1 0 0 1-.25 1z"/></svg>+1 604 555 0172</li>
        <li><svg viewBox="0 0 24 24" aria-hidden="true"><path d="M2 5h20v14H2z M2 5l10 8 10-8" stroke="#fff" stroke-width="1.5"/></svg>rosalind@brightmere.example</li>
        <li><svg viewBox="0 0 24 24" aria-hidden="true"><circle cx="12" cy="12" r="10"/></svg>www.<span class="accent">brightmere</span>.example</li>
      </ul>
    </div>
  </section>

  <section class="card card--brand">
    <div class="brand">
      <span class="brand__dot"></span>
      <span class="brand__name">Brightmere</span>
    </div>
    <p class="tagline">Executive Coaching and Human Capital Strategy</p>
    <p class="web">www.<span class="accent">brightmere</span>.example</p>
  </section>
</body>
</html>
```